Bref créative
Stationery for interior design business
Venmark Interiors, LLC
Simple
Cleo Venmark
Interior Designer
No address on card or stationery
cleo@venmarkinteriors.example
venmarkinteriors.example
Please also include my blog address on the front of the card: cleovenmark.example
Open for design suggestions, but I'd like either the entire logo or only the sphere to appear on the back

```html
<!DOCTYPE html>
<html lang="en">
<head>
<meta charset="utf-8">
<title>Venmark Interiors — Business Card</title>
<link href="https://fonts.googleapis.com/css2?family=Open+Sans:wght@400;600;700&display=swap" rel="stylesheet">
<style>
  :root {
    --page-bg: #e9e7e3;
    --card-white: #ffffff;
    --brand-blue: #3f51a8;
    --brand-blue-deep: #34449a;
    --steel-grey: #5e6066;
    --steel-grey-light: #8a8c92;
    --ink-dark: #2f3034;
    --text-light: #ffffff;
  }
  * { box-sizing: border-box; margin: 0; padding: 0; }
  html, body {
    width: 1200px; height: 900px; overflow: hidden;
    background: var(--page-bg);
    font-family: "Open Sans", Arial, sans-serif;
  }
  .business-card {
    position: absolute; left: 120px; top: 180px;
    width: 960px; height: 540px;
    background: var(--card-white);
    overflow: hidden;
    box-shadow: 0 10px 30px rgba(0,0,0,0.18);
  }
  .brand-lockup {
    position: absolute; left: 0; right: 0; top: 70px;
    display: flex; align-items: center; justify-content: center; gap: 22px;
  }
  .brand-dot {
    width: 96px; height: 96px; border-radius: 50%;
    background: var(--brand-blue);
  }
  .brand-name {
    font-size: 46px; font-weight: 600; color: var(--brand-blue);
    letter-spacing: 1px;
  }
  .accent-strip {
    position: absolute; left: 0; right: 0; top: 262px; height: 22px;
    background: linear-gradient(var(--steel-grey-light), var(--steel-grey));
  }
  .contact-band {
    position: absolute; left: 0; right: 0; top: 284px; height: 226px;
    background: linear-gradient(var(--brand-blue), var(--brand-blue-deep));
    color: var(--text-light);
  }
  .base-strip {
    position: absolute; left: 0; right: 0; top: 510px; height: 30px;
    background: var(--steel-grey);
  }
  .person {
    position: absolute; left: 44px; top: 48px;
  }
  .person-name { font-size: 28px; font-weight: 700; }
  .person-role { font-size: 21px; font-weight: 400; margin-top: 4px; }
  .contact-list {
    position: absolute; left: 548px; top: 22px;
    list-style: none;
  }
  .contact-item {
    display: flex; align-items: center; gap: 14px;
    font-size: 23px; height: 44px;
  }
  .contact-icon { width: 26px; height: 26px; flex: none; }
</style>
</head>
<body>
  <div class="business-card">
    <div class="brand-lockup">
      <div class="brand-dot"></div>
      <div class="brand-name">Venmark Interiors</div>
    </div>

    <div class="accent-strip"></div>

    <div class="contact-band">
      <div class="person">
        <div class="person-name">Cleo Venmark</div>
        <div class="person-role">Interior Designer</div>
      </div>

      <ul class="contact-list">
        <li class="contact-item">
          <svg class="contact-icon" viewBox="0 0 26 26" aria-hidden="true">
            <circle cx="13" cy="13" r="13" fill="#fff"/>
            <path d="M9 7.5l2.2 2.6-1.3 1.6c.8 1.7 2.2 3.1 3.9 3.9l1.6-1.3 2.6 2.2-1.2 1.8c-4.6-.4-8.8-4.6-9.2-9.2z" fill="#3f51a8"/>
          </svg>
          <span>555-014-2273</span>
        </li>
        <li class="contact-item">
          <svg class="contact-icon" viewBox="0 0 26 26" aria-hidden="true">
            <circle cx="13" cy="13" r="13" fill="#fff"/>
            <rect x="6.5" y="8.5" width="13" height="9" rx="1" fill="#3f51a8"/>
            <path d="M6.8 9l6.2 4.6L19.2 9" fill="none" stroke="#fff" stroke-width="1.2"/>
          </svg>
          <span>cleo@venmarkinteriors.example</span>
        </li>
        <li class="contact-item">
          <svg class="contact-icon" viewBox="0 0 26 26" aria-hidden="true">
            <circle cx="13" cy="13" r="13" fill="#fff"/>
            <g fill="none" stroke="#3f51a8" stroke-width="1.4">
              <circle cx="13" cy="13" r="6.5"/>
              <ellipse cx="13" cy="13" rx="2.8" ry="6.5"/>
              <path d="M6.5 13h13"/>
            </g>
          </svg>
          <span>venmarkinteriors.example</span>
        </li>
        <li class="contact-item">
          <svg class="contact-icon" viewBox="0 0 26 26" aria-hidden="true">
            <circle cx="13" cy="13" r="13" fill="#fff"/>
            <g fill="none" stroke="#3f51a8" stroke-width="1.4">
              <circle cx="13" cy="13" r="6.5"/>
              <ellipse cx="13" cy="13" rx="2.8" ry="6.5"/>
              <path d="M6.5 13h13"/>
            </g>
          </svg>
          <span>cleovenmark.example</span>
        </li>
      </ul>
    </div>

    <div class="base-strip"></div>
  </div>
</body>
</html>
```